CD Cover and Disc Design - Beneath the Quiet Willows

Need a cd cover design front, back, and disc design for a singer's Music CD. The client likes impressionism art. The title of the cd is, "Beneath the Quiet Willows" by Marisa Dunleigh.
Make sure that it keeps the viewer wondering what's ahead. So that they can imagine their on road.

This music is a collection of Negro Spirituals. The image should be ethnic containing elements depicting traveling to freedom.

Target Market(s)

Jazz & Classical music lovers. Age range is 40's and up.

Industry/Entity Type

Music Download

Font styles to use
Script

Colors
ec1f27
abd036
fbf289
fac994
3176b5

Requirements
Must have
• Must be colorful and including a road being traveled through.
Nice to have
• Include thought provoking Impressionism style art design
Should not have
• black and white or grayscale imagery.

```html
<!DOCTYPE html>
<html lang="en">
<head>
<meta charset="utf-8">
<title>Beneath the Quiet Willows — CD Package</title>
<link rel="stylesheet" href="https://fonts.googleapis.com/css2?family=Open+Sans:wght@400&family=Marcellus&family=Great+Vibes&display=swap">
<style>
  :root {
    --page: #ffffff;
    --ink: #1e1a14;
    --gold-light: #fbf289;
    --gold: #f3c640;
    --amber: #e59a2a;
    --peach: #fac994;
    --rust: #b8431f;
    --red: #ec1f27;
    --violet: #8d5a9e;
    --leaf: #abd036;
    --cream: #fffbea;
    --script-ice: #e8f6f8;
    --hub: rgba(245, 242, 236, 0.88);
  }
  html, body {
    margin: 0;
    padding: 0;
    width: 1200px;
    height: 1200px;
    overflow: hidden;
    background: var(--page);
  }
  .package {
    position: relative;
    width: 1200px;
    height: 1200px;
  }
  /* Back cover */
  .back-cover {
    position: absolute;
    left: 33px;
    top: 110px;
    width: 569px;
    height: 566px;
  }
  .back-cover__art {
    position: absolute;
    inset: 0;
    background:
      radial-gradient(ellipse 55% 45% at 50% 28%, var(--cream) 0%, rgba(255,250,220,0.85) 40%, rgba(255,240,160,0) 75%),
      linear-gradient(180deg, var(--gold-light) 0%, var(--gold) 38%, #d9a24a 55%, #9b7b62 68%, #c58a48 82%, #7e5f78 100%);
  }
  .back-cover__title {
    position: absolute;
    left: 0;
    right: 0;
    top: 113px;
    margin: 0;
    text-align: center;
    font-family: "Open Sans", sans-serif;
    font-weight: 400;
    font-size: 21px;
    color: var(--ink);
    white-space: nowrap;
  }
  .tracklist {
    position: absolute;
    left: 180px;
    top: 186px;
    margin: 0;
    padding: 0;
    list-style: none;
    font-family: "Open Sans", sans-serif;
    font-size: 17.5px;
    line-height: 22.4px;
    color: var(--ink);
  }
  /* Front cover */
  .front-cover {
    position: absolute;
    left: 619px;
    top: 110px;
    width: 552px;
    height: 566px;
    background: linear-gradient(135deg, var(--rust) 0%, var(--red) 35%, #c85a2a 60%, var(--violet) 85%, var(--leaf) 100%);
  }
  .front-cover__title {
    position: absolute;
    left: 0;
    right: 0;
    top: 28px;
    margin: 0;
    text-align: center;
    white-space: nowrap;
    font-family: "Marcellus", serif;
    font-weight: 400;
    font-size: 26px;
    letter-spacing: 2px;
    line-height: 1;
    color: var(--cream);
    text-shadow: 2px 2px 3px rgba(60, 20, 0, 0.7);
  }
  .front-cover__landscape {
    position: absolute;
    left: 0;
    top: 84px;
    width: 415px;
    height: 482px;
    background:
      radial-gradient(circle at 23% 11%, #ffffff 0%, #fff6c0 8%, rgba(255,240,150,0) 20%),
      linear-gradient(180deg, var(--gold-light) 0%, var(--gold) 35%, #c98b3a 50%, #a7703c 70%, var(--amber) 100%);
  }
  .front-cover__portrait {
    position: absolute;
    left: 255px;
    top: 185px;
    width: 297px;
    height: 381px;
    border-radius: 48% 48% 0 0 / 30% 30% 0 0;
    background: linear-gradient(180deg, #4a2a14 0%, #e3a04a 30%, var(--peach) 50%, #c9812f 75%, #3a2410 100%);
  }
  .front-cover__artist {
    position: absolute;
    left: 28px;
    top: 478px;
    margin: 0;
    white-space: nowrap;
    font-family: "Great Vibes", cursive;
    font-weight: 400;
    font-size: 50px;
    line-height: 1;
    color: var(--script-ice);
    text-shadow: 1px 1px 2px rgba(40, 60, 80, 0.6);
  }
  /* Disc */
  .disc {
    position: absolute;
    left: 194px;
    top: 586px;
    width: 588px;
    height: 588px;
    filter: drop-shadow(0 6px 10px rgba(0, 0, 0, 0.35));
  }
  .disc__title {
    font-family: "Marcellus", serif;
    font-size: 22px;
    letter-spacing: 1px;
    fill: var(--cream);
  }
  .disc__artist {
    font-family: "Great Vibes", cursive;
    font-size: 44px;
    fill: var(--script-ice);
  }
</style>
</head>
<body>
<main class="package">

  <section class="back-cover">
    <div class="back-cover__art" role="img" aria-label="Impressionist painting of golden hills under a hazy glowing sky"></div>
    <h2 class="back-cover__title">BENEATH THE QUIET WILLOWS</h2>
    <ol class="tracklist">
      <li>&nbsp;&nbsp;1........ Song number 1</li>
      <li>&nbsp;&nbsp;2. .......Song number 2</li>
      <li>&nbsp;&nbsp;3. .......Song number 3</li>
      <li>&nbsp;&nbsp;4. .......Song number 4</li>
      <li>&nbsp;&nbsp;5. .......Song number 5</li>
      <li>&nbsp;&nbsp;6........ Song number 6</li>
      <li>&nbsp;&nbsp;7. .......Song number 7</li>
      <li>&nbsp;&nbsp;8........ Song number 8</li>
      <li>&nbsp;&nbsp;9. .......Song number 9</li>
      <li>10. .......Song number 10</li>
      <li>11........ Song number 11</li>
      <li>12. .......Song number 12</li>
    </ol>
  </section>

  <section class="front-cover" role="img" aria-label="Impressionist garden of red, violet and green flowers">
    <h1 class="front-cover__title">BENEATH THE QUIET WILLOWS</h1>
    <div class="front-cover__landscape" role="img" aria-label="Impressionist painting of a bright sun over golden rolling hills"></div>
    <div class="front-cover__portrait" role="img" aria-label="Painted portrait of the singer smiling"></div>
    <p class="front-cover__artist">Marisa Dunleigh</p>
  </section>

  <svg class="disc" viewBox="0 0 588 588" aria-label="CD disc label">
    <defs>
      <linearGradient id="disc-paint" x1="0" y1="0" x2="0.6" y2="1">
        <stop offset="0" stop-color="#d9892a"/>
        <stop offset="0.3" stop-color="#f0b63a"/>
        <stop offset="0.55" stop-color="#c97a34"/>
        <stop offset="0.75" stop-color="#9a5c8e"/>
        <stop offset="1" stop-color="#b8582a"/>
      </linearGradient>
      <linearGradient id="disc-portrait" x1="0" y1="0" x2="0" y2="1">
        <stop offset="0" stop-color="#4a2a14"/>
        <stop offset="0.25" stop-color="#e3a04a"/>
        <stop offset="0.55" stop-color="#fac994"/>
        <stop offset="1" stop-color="#8a5520"/>
      </linearGradient>
      <clipPath id="disc-clip"><circle cx="294" cy="294" r="284"/></clipPath>
    </defs>
    <g clip-path="url(#disc-clip)">
      <rect width="588" height="588" fill="url(#disc-paint)" role="img" aria-label="Impressionist willow trees and wildflowers"/>
      <ellipse cx="470" cy="440" rx="170" ry="220" fill="url(#disc-portrait)" role="img" aria-label="Painted portrait of the singer smiling"/>
    </g>
    <circle cx="294" cy="294" r="110" fill="var(--hub)"/>
    <circle cx="294" cy="294" r="36" fill="#ffffff"/>
    <text class="disc__title" x="294" y="130" text-anchor="middle" textLength="400" lengthAdjust="spacingAndGlyphs">BENEATH THE QUIET WILLOWS</text>
    <text class="disc__artist" x="96" y="462">Marisa Dunleigh</text>
  </svg>

</main>
</body>
</html>
```